body therapist

I need to offer my services as a massage therapist at home, acclimating customer space aroma candles with music and everything else to bring comfort. 8 offer rituals like this: relaxing ritual, purifying ritual, ritual breast, facial and body cleansing ritual organic, ritual man, ritual feet, slimming ritual. Naraja handling colors, seawater, green, lavender

Target Market(s)

men and women, tired, stressed, looking for something new

Font styles to use
Decorative
Script

Colors
f37122
0493ce
abd037

Requirements
Must have
• detailing each massage
Nice to have
• simple and elegant

```html
<!DOCTYPE html>
<html lang="es">
<head>
<meta charset="utf-8">
<title>Rituales de Relajamiento – Masaje a domicilio</title>
<link href="https://fonts.googleapis.com/css2?family=Pinyon+Script&family=EB+Garamond:ital,wght@0,400;0,500;1,400&family=Libre+Baskerville:wght@700&family=Lora:ital,wght@1,500&display=swap" rel="stylesheet">
<style>
  :root{
    --bg:#a6ddd6;
    --paper:#ffffff;
    --taupe:#d8cbc5;
    --rule:#b8a29a;
    --ink:#3a2a26;
    --ink-dark:#2a1a16;
    --skin:#c98a62;
    --warm:#e9d6c4;
    --petal:#d68f84;
  }
  *{margin:0;padding:0;box-sizing:border-box}
  html,body{width:1200px;height:1200px;overflow:hidden;background:var(--bg)}
  .brochure{position:absolute;left:30px;top:130px;width:1140px;height:940px;background:var(--paper);box-shadow:0 18px 40px rgba(0,0,0,.12)}
  .page{position:absolute;top:0;height:100%;width:570px}
  .page-left{left:0}
  .page-right{left:570px;border-left:1px solid #e6e0dd}
  .benefits-title{position:absolute;left:50px;top:38px;font-family:"Pinyon Script",cursive;font-size:34px;color:var(--ink);white-space:nowrap}
  .body-copy{font-family:"EB Garamond",serif;font-size:14px;line-height:1.22;color:var(--ink)}
  .intro{position:absolute;left:50px;top:100px;width:476px}
  .intro p{margin-bottom:12px}
  .dropcap{float:left;font-size:48px;line-height:38px;margin-right:6px;color:var(--ink-dark);font-weight:500}
  .col{position:absolute;width:232px;text-align:justify}
  .c1{left:50px;top:252px}
  .c2{left:300px;top:252px}
  .c3{left:50px;top:705px}
  .c4{left:300px;top:705px}
  .col p{margin-bottom:14px}
  .rule-top{position:absolute;left:0;top:381px;width:100%;height:5px;background:var(--taupe)}
  .photo-row{position:absolute;left:0;top:387px;width:1140px;height:298px}
  .photo{position:absolute;top:0;height:100%}
  .photo-back{left:0;width:266px;background:linear-gradient(120deg,#b3704c,#d9a07a 55%,#e8c9a8)}
  .photo-couple{left:266px;width:480px;background:linear-gradient(100deg,#e5c6a6,#f3e5d4 50%,#f6efe6)}
  .photo-petals{left:746px;width:394px;background:linear-gradient(120deg,#8a5a3c,#c98a62 45%,#d99a8a 80%,#b86a5a)}
  .services-band{position:absolute;left:0;top:86px;width:570px;height:301px;background:var(--taupe);border-top:4px solid var(--rule)}
  .mark{position:absolute;left:228px;top:28px;width:110px;height:62px;border-radius:50% 50% 40% 40%;background:linear-gradient(180deg,#e7ddd8,#c8b8b0)}
  .services-title{position:absolute;left:30px;top:130px;font-family:"Lora",serif;font-style:italic;font-weight:500;font-size:19px;color:var(--ink-dark)}
  .list{position:absolute;font-family:"Libre Baskerville",serif;font-weight:700;font-size:15px;line-height:24.5px;color:var(--ink-dark);list-style:none}
  .services{left:30px;top:158px}
  .services .indent{padding-left:26px}
  .colors{left:334px;top:237px}
  .contact-band{position:absolute;left:0;top:685px;width:570px;height:58px;background:var(--taupe);border-bottom:4px solid var(--rule);text-align:center;font-family:"Lora",serif;font-style:italic;font-weight:500;font-size:19px;line-height:56px;color:var(--ink-dark)}
  .promise{position:absolute;left:16px;top:765px;width:270px;text-align:center;font-family:"Lora",serif;font-style:italic;font-weight:500;font-size:19px;line-height:25px;color:var(--ink-dark)}
  .phone{position:absolute;left:300px;top:768px;font-family:"Lora",serif;font-style:italic;font-weight:500;font-size:30px;color:var(--ink-dark);display:flex;align-items:center;gap:8px;white-space:nowrap}
  .hours{position:absolute;left:330px;top:818px;width:220px;text-align:center;font-family:"Lora",serif;font-style:italic;font-weight:500;font-size:19px;line-height:26px;color:var(--ink-dark)}
</style>
</head>
<body>
<div class="brochure">
  <section class="page page-left">
    <h1 class="benefits-title">Estos son los 6 beneficios de un masaje relajante</h1>
    <div class="intro body-copy">
      <p><span class="dropcap">E</span>l estrés de nuestro día a día puede afectarte, y mucho, tanto física como psicológicamente.</p>
      <p>Lo que te proponemos no es la solución definitiva, pero sí puede ayudarte a recuperar fuerzas para afrontar tu rutina diaria.</p>
      <p>Y es que un masaje relajante tienes más beneficios para nuestra salud de los que pensábamos:</p>
    </div>
    <div class="col c1 body-copy"><p>1. Con un masaje relajante, conseguimos terminar con problemas musculares como las contracturas, provocados por una mala postura prolongada, un movimiento brusco o incluso por el estrés.</p></div>
    <div class="col c2 body-copy"><p>2. Un masaje relajante mejora la circulación sanguínea en todo el cuerpo y, como consecuencia, se produce un aumento del aporte de oxígeno en los tejidos y los órganos, beneficiando nuestra salud en general.</p></div>
    <div class="rule-top"></div>
    <div class="col c3 body-copy">
      <p>3. Aumenta el flujo del líquido linfático mejorando nuestro sistema linfático, el encargado que terminar con las toxinas y otros contaminantes de nuestro cuerpo.</p>
      <p>4. Al eliminar las toxinas del cuerpo y las células muertas, el masaje corporal nos ayuda a tener una piel más sana y hermosa.</p>
    </div>
    <div class="col c4 body-copy">
      <p>5. Promueve la respiración profunda y lenta lo que nos beneficia en cuerpo y mente. No sólo aumenta el nivel del oxígeno en nuestro cuerpo sino que además nos reja y aplaca la ansiedad.</p>
      <p>6. Al proporcionarnos esa sensación de relax, este tipo de masajes nos ayudan a disipar las tensiones y las preocupaciones del día a día.</p>
    </div>
  </section>

  <section class="page page-right">
    <div class="services-band"></div>
    <div class="mark" role="img" aria-label="Ilustración de una persona recibiendo masaje"></div>
    <h2 class="services-title">8 Servicios de Relajamiento</h2>
    <ul class="list services">
      <li>1. Ritual Relajante</li>
      <li>2. Ritual Purificante</li>
      <li>3. Ritual Mama</li>
      <li>4. Ritual Limpieza Organica</li>
      <li class="indent">Facial y Corporal</li>
      <li>5. Ritual Hombre</li>
      <li>5. Rrtual Pies</li>
      <li>6. Ritual Adelgazante.</li>
    </ul>
    <ul class="list colors">
      <li>Manejando colores</li>
      <li>1. Naraja</li>
      <li>1. Agua Marina</li>
      <li>1. Verde</li>
      <li>1. Lavanda</li>
    </ul>
    <div class="contact-band">Contactanos para hacer una cita a domicilio</div>
    <p class="promise">Nos esforzamos por ofrecer la mejor experiencia profecional de masaje que sea posible.</p>
    <p class="phone"><svg width="22" height="24" viewBox="0 0 24 24" aria-hidden="true"><path fill="#2a1a16" d="M6.6 2.5c.6-.4 1.4-.3 1.8.3l2.2 3.3c.4.6.3 1.3-.2 1.8L8.9 9.2c.9 2.4 3.4 5 5.8 5.9l1.3-1.5c.5-.5 1.2-.6 1.8-.2l3.3 2.2c.6.4.7 1.2.3 1.8l-1.3 2c-.8 1.2-2.3 1.7-3.7 1.2C10.3 18.5 5.5 13.7 3.4 7.6c-.5-1.4 0-2.9 1.2-3.7z"/></svg>1 800-555-0142</p>
    <p class="hours">Lunes a Sabado<br>8 a 21 hrs.</p>
  </section>

  <div class="photo-row">
    <div class="photo photo-back" role="img" aria-label="Foto de manos dando masaje en la espalda con orquídeas y velas"></div>
    <div class="photo photo-couple" role="img" aria-label="Foto de una pareja relajada en camillas de spa con velas encendidas"></div>
    <div class="photo photo-petals" role="img" aria-label="Foto de una mujer recibiendo masaje rodeada de pétalos de rosa"></div>
  </div>
</div>
</body>
</html>
```